Partial Wrap Design for Painting Company

Need a wrap design that we can adapt to several vans. The immediate need is for 2016 Harlow KT300 and 2009 Brandt M-340. Vehicles are white.
We want a PARTIAL wrap (not full coverage).
We want to show;
- our phone number; (927) 555-LARK
- our website address; www.larkpainting.example
- our services; Interior - Exterior - Cabinet
Any questions? Feel free to ask.

Target Market(s)

Homeowners

Industry/Entity Type

Painting

```html
<!DOCTYPE html>
<html lang="en">
<head>
<meta charset="utf-8">
<title>Lark Painting – Rear Door Partial Wrap</title>
<link rel="stylesheet" href="https://fonts.googleapis.com/css2?family=Barlow+Condensed:wght@600;700&display=swap">
<style>
  :root {
    --canvas: #ffffff;
    --vehicle-white: #ecece8;
    --wrap-dark: #2b2a2a;
    --stripe-orange: #f39220;
    --stripe-red: #d82c2a;
    --accent-blue: #3a9ad9;
    --accent-green: #9bc83b;
    --ink-light: #ffffff;
  }
  * { margin: 0; padding: 0; box-sizing: border-box; }
  html, body {
    width: 1200px; height: 1066px; overflow: hidden;
    background: var(--canvas);
  }
  .wrap-panel {
    position: relative; width: 1200px; height: 1066px;
    font-family: "Barlow Condensed", "Arial Narrow", sans-serif;
    color: var(--ink-light);
  }
  .wrap-shape { position: absolute; inset: 0; }
  .text-column {
    position: absolute; left: 500px; width: 546px;
    text-align: center; white-space: nowrap;
  }
  .brand-block { top: 300px; }
  .brand-name {
    font-size: 118px; font-weight: 700; line-height: 1;
    letter-spacing: 4px;
  }
  .brand-sub {
    margin-top: 14px;
    font-size: 38px; font-weight: 700; line-height: 1;
    letter-spacing: 22px; padding-left: 22px;
  }
  .services {
    position: absolute; left: 553px; width: 440px; top: 486px;
    display: flex; justify-content: space-between; align-items: center;
    font-size: 30px; font-weight: 600; line-height: 1; white-space: nowrap;
  }
  .service { padding-bottom: 6px; border-bottom: 4px solid; }
  .service--interior { border-color: var(--accent-blue); }
  .service--exterior { border-color: var(--stripe-orange); }
  .service--cabinet { border-color: var(--stripe-red); }
  .service-dot {
    width: 6px; height: 6px; border-radius: 50%;
    background: var(--accent-green); margin-top: -8px;
  }
  .phone {
    top: 556px;
    font-size: 72px; font-weight: 700; line-height: 1;
  }
  .website {
    top: 644px;
    font-size: 30px; font-weight: 600; line-height: 1;
  }
  .tagline {
    top: 740px;
    font-size: 58px; font-weight: 700; line-height: 62px;
  }
</style>
</head>
<body>
<main class="wrap-panel">
  <svg class="wrap-shape" width="1200" height="1066" viewBox="0 0 1200 1066" aria-hidden="true">
    <defs>
      <clipPath id="door-outline">
        <rect x="60" y="60" width="1080" height="946" rx="80"/>
      </clipPath>
    </defs>
    <g clip-path="url(#door-outline)">
      <rect class="vehicle-body" x="60" y="60" width="1080" height="946" fill="var(--vehicle-white)"/>
      <path class="stripe-orange" transform="translate(-34 0)"
            d="M734 60 L1180 60 L1180 1006 L103 1006 C330 900 360 650 450 500 S 630 120 734 60 Z"
            fill="var(--stripe-orange)"/>
      <path class="stripe-red" transform="translate(-17 0)"
            d="M734 60 L1180 60 L1180 1006 L103 1006 C330 900 360 650 450 500 S 630 120 734 60 Z"
            fill="var(--stripe-red)"/>
      <path class="wrap-field"
            d="M734 60 L1180 60 L1180 1006 L103 1006 C330 900 360 650 450 500 S 630 120 734 60 Z"
            fill="var(--wrap-dark)"/>
    </g>
  </svg>

  <div class="text-column brand-block">
    <div class="brand-name">LARK</div>
    <div class="brand-sub">PAINTING</div>
  </div>

  <div class="services">
    <span class="service service--interior">INTERIOR</span>
    <span class="service-dot"></span>
    <span class="service service--exterior">EXTERIOR</span>
    <span class="service-dot"></span>
    <span class="service service--cabinet">CABINET</span>
  </div>

  <div class="text-column phone">(927) 555-LARK</div>
  <div class="text-column website">www.larkpainting.example</div>

  <p class="text-column tagline">PROFESSIONAL<br>HOUSE PAINTERS<br>FOR YOUR HOME</p>
</main>
</body>
</html>
```